WP website design (Carrowind)

We need a wordpress design for an established auction and real estate company based in Florida. The winning design will incorporate a professional color scheme with company logo in a clean layout. The design needs to consider that this will be developed on a responsive theme. Colors are those that will highlight the logo.

Industry/Entity Type

Real Estate

Font styles to use
Serif
Sans Serif

Colors

Designer to choose colors to be used in the design.

Requirements
Must have
• Navigation:
1) Home
2) Auctions
3) Online Auctions
4) About Us
5) Services
6) Real Estate Listings
7) References
8) Contact Us

Colors will be blue (#000066) / red (#B10000) and black or other complementary color. Tagline to be used "Since 1977, Proven Results." Slideshow to be placed in the header or body of home page - please use stock real estate image.

Widgets: 1) Email Sign-up 2) Social media icons for Chirpa and TradeLoop 3) Featured Listings 4) Testimonials 5) Register button

Footer will have smaller company logo, attached logos and contact info:
Phone: (555) 218-6049 Mobile: (555) 762-3815
Email: marlacarrowind@plexmail.example
Address: 48 E. Thornbury Lane, Ste 310, Pensacola, FL 32599
Nice to have
• Use of a drop down menu:
Auctions-
1) Upcoming Auctions
2) Past Auctions

```html
<!DOCTYPE html>
<html lang="en">
<head>
<meta charset="utf-8">
<title>Carrowind Auctions</title>
<link rel="stylesheet" href="https://fonts.googleapis.com/css2?family=Open+Sans:ital,wght@0,400;0,600;0,700;1,400&family=Arimo:wght@400;700&display=swap">
<style>
:root{
  --navy:#1e1f86;
  --red:#c8161d;
  --red-text:#b10000;
  --ink:#222;
  --panel:#efefef;
  --footer:#2a2a2a;
  --white:#fff;
  --photo-hero-a:#8fb36a;
  --photo-hero-b:#6f9a4a;
  --photo-a:#a9a99f;
  --photo-b:#8f9484;
}
*{margin:0;padding:0;box-sizing:border-box}
html,body{width:980px;height:1200px;overflow:hidden;background:var(--white)}
body{position:relative;font-family:"Arimo",Arial,sans-serif;color:var(--ink)}
.abs{position:absolute}

.brand{left:106px;top:26px;display:flex;align-items:center;gap:12px}
.brand-mark{width:54px;height:54px;background:var(--navy)}
.brand-name{font-family:"Open Sans",sans-serif;font-weight:700;font-size:30px;color:var(--navy);letter-spacing:.5px}
.connect{left:608px;top:55px;display:flex;align-items:center;gap:10px}
.connect-label{font-family:"Open Sans",sans-serif;font-weight:600;font-size:18px;color:#444;letter-spacing:.5px}
.social{display:flex;align-items:center;gap:4px;font-family:"Open Sans",sans-serif;font-size:12px;font-weight:600;color:var(--navy)}
.social i{width:12px;height:12px;background:var(--navy);display:block}

.nav{left:0;top:112px;width:980px;height:41px;background:var(--navy);display:flex;align-items:center;padding-left:85px}
.nav a{color:var(--white);text-decoration:none;font-family:"Open Sans",sans-serif;font-weight:600;font-size:11.5px;padding:0 15px;line-height:26px;border-right:1px solid #4c4da6}
.nav a:last-child{border-right:0}

.hero{left:0;top:153px;width:980px;height:298px;background:linear-gradient(135deg,var(--photo-hero-a),var(--photo-hero-b))}
.dropdown{left:156px;top:160px;width:131px;background:var(--navy);border-radius:3px;padding:3px 0;box-shadow:0 2px 4px rgba(0,0,0,.3)}
.dropdown a{display:block;color:var(--white);text-decoration:none;font-family:"Open Sans",sans-serif;font-size:11.5px;padding:6px 13px}
.dropdown a.active{background:var(--red)}
.tagline{left:114px;top:392px;width:522px;height:43px;background:rgba(70,80,30,.6);color:var(--white);font-family:"Open Sans",sans-serif;font-size:26px;line-height:43px;padding-left:43px;letter-spacing:.5px}
.signup{left:642px;top:164px;width:228px;height:228px;background:linear-gradient(135deg,#d51d24,#b8121a);padding:16px 21px}
.signup h2{font-family:"Open Sans",sans-serif;font-weight:400;color:var(--white);font-size:19px;margin-bottom:16px}
.signup .field{height:28px;background:linear-gradient(#fff,#e8e8e8);margin-bottom:20px;font-size:11px;color:#555;line-height:28px;padding-left:8px}
.signup .btn{display:inline-block;background:#1b1b1b;color:var(--white);font-family:"Open Sans",sans-serif;font-weight:700;font-size:13.5px;padding:4px 5px;border-radius:3px;margin-top:-4px}
.register{left:642px;top:392px;width:228px;height:43px;background:linear-gradient(#333,#000);color:var(--white);font-family:"Open Sans",sans-serif;font-weight:700;font-size:16px;line-height:43px;text-align:right;padding-right:22px;letter-spacing:.5px}

.section-title{font-family:"Open Sans",sans-serif;font-weight:400;color:var(--red-text);font-size:19px;letter-spacing:.3px}
.section-title.bold{font-weight:700}
.card{left:97px;width:504px;height:230px;background:var(--panel)}
.card .photo{position:absolute;left:11px;top:15px;width:187px;height:156px;background:linear-gradient(135deg,var(--photo-a),var(--photo-b))}
.card .btn{position:absolute;top:185px;height:25px;color:var(--white);font-size:13.5px;line-height:25px;display:flex;align-items:center;gap:7px;padding-left:8px}
.card .btn.details{left:11px;width:80px;background:#222}
.card .btn.gallery{left:110px;width:88px;background:var(--navy)}
.icon-search{width:11px;height:11px;border:2px solid #ccc;border-radius:50%}
.icon-gallery{width:13px;height:11px;border:2px solid #fff}
.info{position:absolute;left:210px;width:282px;background:var(--white);border:1px solid #ddd;border-radius:3px;padding:9px 9px}
.info h3{font-weight:400;color:var(--red-text);font-size:13px;margin-bottom:5px}
.info p{font-size:11px;line-height:16px}
.info .meta{font-size:10px;line-height:13px}

.featured{left:625px;top:523px;width:259px;height:210px;background:var(--panel);padding:16px 17px}
.featured h4{font-size:11.5px;font-weight:700;margin-bottom:9px}
.featured .photo{width:217px;height:97px;margin-bottom:10px;background:linear-gradient(135deg,#a49a88,#7f9868)}
.featured p{font-size:10px;line-height:15px}
.featured p.sub{font-size:11px;margin-top:6px}

.testimonial{left:626px;top:789px;width:258px;height:209px;background:var(--panel);padding:16px 15px 16px 19px}
.quote-mark{color:#bbb;font-size:18px;font-family:Georgia,serif;line-height:14px}
.testimonial blockquote{font-family:"Open Sans",sans-serif;font-style:italic;font-size:10.6px;line-height:16.4px;color:#555;letter-spacing:.25px}
.testimonial blockquote span{padding-left:18px}
.testimonial cite{display:block;text-align:right;color:var(--red-text);font-family:"Open Sans",sans-serif;font-size:11.5px;margin-top:12px;padding-right:10px}

.footer{left:0;top:1029px;width:980px;height:138px;background:var(--footer)}
.contact{left:87px;top:1058px;color:var(--white);font-size:11px;line-height:18px}
.badge{background:#8a8a8a;opacity:.75}
.footer-brand{left:725px;top:1098px;display:flex;align-items:center;gap:10px}
.footer-brand .brand-mark{width:40px;height:40px;background:#9a9a9a}
.footer-brand .brand-name{color:#a8a8a8;font-size:22px}
.copyright{left:0;top:1167px;width:980px;height:33px;background:var(--navy);color:var(--white);font-size:11px;text-align:center;line-height:33px}
</style>
</head>
<body>

<header>
  <div class="abs brand"><span class="brand-mark"></span><span class="brand-name">Carrowind</span></div>
  <div class="abs connect">
    <span class="connect-label">STAY CONNECTED:</span>
    <span class="social"><i></i>Chirpa</span>
    <span class="social"><i></i>TradeLoop</span>
  </div>
</header>

<nav class="abs nav">
  <a href="#">HOME</a><a href="#">AUCTIONS</a><a href="#">ONLINE AUCTIONS</a><a href="#">ABOUT US</a><a href="#">SERVICES</a><a href="#">REAL ESTATE LISTINGS</a><a href="#">REFERENCES</a><a href="#">CONTACT US</a>
</nav>

<div class="abs hero" role="img" aria-label="Stock photo of a white single-storey house with palm trees and lawn"></div>
<div class="abs dropdown"><a class="active" href="#">Upcoming Auctions</a><a href="#">Past Auctions</a></div>
<div class="abs tagline">SINCE 1977, PROVEN RESULTS</div>
<form class="abs signup">
  <h2>Email sign-up</h2>
  <div class="field">Name</div>
  <div class="field">Email</div>
  <span class="btn">Subscribe</span>
</form>
<div class="abs register">REGISTER NOW! &nbsp;&gt;&gt;</div>

<h2 class="abs section-title bold" style="left:100px;top:484px">UPCOMING AUCTIONS</h2>

<article class="abs card" style="top:523px">
  <div class="photo" role="img" aria-label="Photo of a large two-storey grey house"></div>
  <span class="btn details"><i class="icon-search"></i>Details</span>
  <span class="btn gallery"><i class="icon-gallery"></i>Gallery</span>
  <div class="info" style="top:13px;height:77px">
    <h3>Auction 1</h3>
    <p>Lorem Ipsum is simply dummy text of the printing and typesetting industry.</p>
  </div>
  <div class="info" style="top:104px;height:116px">
    <h3>Online Bidding Only</h3>
    <p class="meta">Began:&nbsp; Friday, May 24, 2013 at 10:06 AM EDT</p>
    <p class="meta" style="margin-top:10px"><b>Location</b><br>1620 Larkmoor Ln. NW Cedar Rapids, IA 52499</p>
  </div>
</article>

<article class="abs card" style="top:770px">
  <div class="photo" role="img" aria-label="Photo of a beige two-storey house with balconies" style="--photo-a:#b7a68c;--photo-b:#8c9a78"></div>
  <span class="btn details"><i class="icon-search"></i>Details</span>
  <span class="btn gallery"><i class="icon-gallery"></i>Gallery</span>
  <div class="info" style="top:13px;height:77px">
    <h3>Auction 1</h3>
    <p>Lorem Ipsum is simply dummy text of the printing and typesetting industry.</p>
  </div>
  <div class="info" style="top:104px;height:116px">
    <h3>Online Bidding Only</h3>
    <p class="meta">Began:&nbsp; Friday, May 24, 2013 at 10:06 AM EDT</p>
    <p class="meta" style="margin-top:10px"><b>Location</b><br>1620 Larkmoor Ln. NW Cedar Rapids, IA 52499</p>
  </div>
</article>

<h2 class="abs section-title" style="left:625px;top:484px">FEATURED LISTINGS</h2>
<aside class="abs featured">
  <h4>Multi Estate &amp; Consignment Auction</h4>
  <div class="photo" role="img" aria-label="Photo of a house with porch and flower garden"></div>
  <p><b>Start Date/ Time:</b> Saturday, April 13,<br>2013 At 10:00 Am</p>
  <p class="sub">Multi Estate &amp; Consignment Auction</p>
</aside>

<h2 class="abs section-title" style="left:626px;top:754px">TESTIMONIALS</h2>
<aside class="abs testimonial">
  <div class="quote-mark">&ldquo;</div>
  <blockquote><span></span>Lorem Ipsum has been the industry's standard dummy text ever since the 1500s, when an unknown printer took a galley of type and scrambled it to make a type speci men book.It has survived not only five centuries, but also the leap into electronic typesetting, remaining essentially unchanged.</blockquote>
  <div class="quote-mark" style="padding-left:72px">&rdquo;</div>
  <cite>Dana Whitfield</cite>
</aside>

<footer>
  <div class="abs footer"></div>
  <div class="abs contact">
    <b>Phone:</b> (555) 218-6049<br>
    <b>Mobile:</b> (555) 762-3815<br>
    <b>Email:</b> marlacarrowind@plexmail.example<br>
    <b>Address:</b> 48 E. Thornbury Lane,<br>Ste 310, Pensacola, FL 32599
  </div>
  <div class="abs badge" style="left:331px;top:1062px;width:46px;height:36px"></div>
  <div class="abs badge" style="left:384px;top:1062px;width:28px;height:34px"></div>
  <div class="abs badge" style="left:421px;top:1063px;width:115px;height:34px"></div>
  <div class="abs badge" style="left:545px;top:1060px;width:72px;height:38px"></div>
  <div class="abs badge" style="left:346px;top:1110px;width:142px;height:32px"></div>
  <div class="abs badge" style="left:506px;top:1115px;width:94px;height:26px"></div>
  <div class="abs footer-brand"><span class="brand-mark"></span><span class="brand-name">Carrowind</span></div>
  <div class="abs copyright">Copyright © 2014 <u>Carrowind Auctions</u> All Rights Reserved.</div>
</footer>

</body>
</html>
```